Upscale business cards needed for family office

We would like professional business cards created for employees of our family office. Relatively simple and straightforward, but also with a unique element to set them apart. Probably stick with neutral and simple colors that mesh well with the colors in the logo. We need space for the traditional elements, including name, title, address, email/phone number.

Industry/Entity Type

Business

Contact Information for Business Card

Space for name, title, phone number, email, address

```html
<!DOCTYPE html>
<html lang="en">
<head>
<meta charset="utf-8">
<title>Ashby &amp; Vale – Business Cards</title>
<link href="https://fonts.googleapis.com/css2?family=Quicksand:wght@400;500&display=swap" rel="stylesheet">
<style>
  :root {
    --bg: #e4e4e2;
    --card-white: #fbfbfa;
    --card-dark: #3a3a3b;
    --ink: #2b3238;
    --ink-soft: #4a4f54;
    --accent: #1a8fd0;
    --frame: #9a9c9e;
    --frame-dark: #8d8f91;
    --mark-on-dark: #c9ced2;
  }
  * { margin: 0; padding: 0; box-sizing: border-box; }
  html, body { width: 1200px; height: 1021px; overflow: hidden; }
  body {
    background: var(--bg);
    font-family: "Quicksand", sans-serif;
    position: relative;
  }
  .card {
    position: absolute;
    width: 620px;
    height: 354px;
    border-radius: 3px;
    box-shadow: 0 10px 26px rgba(0,0,0,0.18);
  }
  .card-front { left: 120px; top: 110px; background: var(--card-white); }
  .card-back { left: 460px; top: 560px; background: var(--card-dark); }

  .brand-frame {
    position: absolute;
    display: flex;
    align-items: center;
    justify-content: center;
    text-align: center;
    color: var(--ink);
    font-weight: 500;
  }
  .card-front .brand-frame {
    right: 36px; top: 30px;
    width: 132px; height: 132px;
    border: 3px solid var(--frame);
    font-size: 22px;
    line-height: 1.15;
  }
  .card-back .brand-frame {
    left: 50%; top: 50%;
    transform: translate(-50%, -50%);
    width: 190px; height: 190px;
    border: 3px solid var(--frame-dark);
    color: var(--mark-on-dark);
    font-size: 30px;
    line-height: 1.15;
  }

  .identity {
    position: absolute;
    left: 46px; top: 186px;
    padding-left: 14px;
    border-left: 6px solid var(--accent);
  }
  .identity .name { font-size: 30px; font-weight: 400; color: var(--ink); line-height: 1.05; }
  .identity .title { font-size: 16px; color: var(--accent); margin-top: 2px; }

  .contact-list {
    position: absolute;
    left: 52px; top: 262px;
    list-style: none;
    font-size: 15px;
    color: var(--ink-soft);
    line-height: 1.3;
  }
  .contact-list li { display: flex; align-items: flex-start; gap: 9px; margin-bottom: 3px; }
  .contact-list svg { width: 13px; height: 13px; margin-top: 3px; flex: none; fill: var(--accent); }
</style>
</head>
<body>
  <section class="card card-front">
    <div class="brand-frame">Ashby<br>&amp; Vale</div>

    <div class="identity">
      <p class="name">Your Name</p>
      <p class="title">Job Title</p>
    </div>

    <ul class="contact-list">
      <li>
        <svg viewBox="0 0 24 24" aria-hidden="true"><path d="M12 1a8 8 0 0 0-8 8c0 6 8 14 8 14s8-8 8-14a8 8 0 0 0-8-8zm0 11a3 3 0 1 1 0-6 3 3 0 0 1 0 6z"/></svg>
        <span>00, Street Name<br>City, State 0000</span>
      </li>
      <li>
        <svg viewBox="0 0 24 24" aria-hidden="true"><path d="M6.6 10.8a15 15 0 0 0 6.6 6.6l2.2-2.2a1 1 0 0 1 1-.25 11.4 11.4 0 0 0 3.6.57 1 1 0 0 1 1 1V20a1 1 0 0 1-1 1A17 17 0 0 1 3 4a1 1 0 0 1 1-1h3.5a1 1 0 0 1 1 1c0 1.25.2 2.45.57 3.57a1 1 0 0 1-.25 1z"/></svg>
        <span>phone number</span>
      </li>
      <li>
        <svg viewBox="0 0 24 24" aria-hidden="true"><path d="M2 5h20v14H2z" fill="none"/><path d="M2 5h20v2l-10 6L2 7zm0 4 10 6 10-6v10H2z"/></svg>
        <span>youremail@xyz.com</span>
      </li>
    </ul>
  </section>

  <section class="card card-back">
    <div class="brand-frame">Ashby<br>&amp; Vale</div>
  </section>
</body>
</html>
```